Business Card Design Project for Female Personal Trainer

I need a business card design to appeal to female clients for my personal training and group fitness boot camp business called 'LumaStride Studio'. It should be girly, fun and have an active/healthy pic or figure incorporated into the business name.

Target Market(s)

- Females 20-65yrs

Industry/Entity Type

Training

Font styles to use
Serif
Sans Serif

Colors
e34197
e567a6

Requirements
Must have
• First Side of Business Card Details :

Odette Calvo
MASTER PERSONAL TRAINER
Cert III & Cert IV in Fitness
Senior First Aid
Mobile: 0493 507 618
Email: lumastride@quellmail.test
Facebook: LumaStride Studio

* Mobile Personal Training *Individual Sessions *Bootcamp *Weight-loss and Toning

Second Side of Business Card I want to offer a free personal consult:
Something like this:

Need direction with your health & fitness goals?

Call now for your free 1 on 1 Personal Training Session with full consultation

Nice to have
• Have a sub-heading for example:

'Promoting healthy living through fitness & nutrition'

- have the colour pink or blue (to appeal to a female)

- a picture/motif//logo attached (sometimes a picture paints a thousand words)

Should not have
• * picture of a person with big muscles or appeal to a man (I'm training women only)

* should not be busy or crammed up look (if I've added to much info above please just use to your discretion).

```html
<!DOCTYPE html>
<html lang="en">
<head>
<meta charset="utf-8">
<title>LumaStride Studio – Business Card</title>
<link rel="stylesheet" href="https://fonts.googleapis.com/css2?family=Arimo:wght@400;700&family=Didact+Gothic&display=swap">
<style>
  :root {
    --pink-bg: #f9d5e7;
    --pink-deep: #e34197;
    --pink-soft: #e567a6;
    --pink-line: #ee6d92;
    --aqua: #d8f3f1;
    --leaf: #7fd3c6;
    --ink: #1c1c1c;
    --white: #ffffff;
  }
  * { box-sizing: border-box; margin: 0; padding: 0; }
  html, body {
    width: 1021px;
    height: 1200px;
    overflow: hidden;
    background: var(--white);
  }
  .canvas {
    position: relative;
    width: 1021px;
    height: 1200px;
    background: var(--white);
    font-family: "Didact Gothic", "Arimo", sans-serif;
    color: var(--ink);
  }
  .card {
    position: absolute;
    left: 0;
    width: 1021px;
    background: var(--pink-bg);
    overflow: hidden;
  }
  .card--front { top: 0; height: 585px; }
  .card--back { top: 613px; height: 587px; }

  .backdrop { position: absolute; inset: 0; }

  .figure-art {
    position: absolute;
    left: 50px;
    top: 0;
    width: 330px;
    height: 585px;
    border-radius: 0 0 60% 40%;
    background: linear-gradient(160deg, rgba(238,109,146,0.35), rgba(229,103,166,0.08) 70%);
  }
  .leaf-art {
    position: absolute;
    left: 40px;
    top: 450px;
    width: 110px;
    height: 70px;
    border-radius: 50%;
    background: radial-gradient(ellipse at center, rgba(127,211,198,0.75), rgba(127,211,198,0) 72%);
  }

  .brand {
    position: absolute;
    left: 420px;
    top: 14px;
    width: 300px;
    text-align: center;
    color: var(--pink-deep);
    font-weight: 400;
  }
  .brand__name { display: block; font-size: 64px; line-height: 1; letter-spacing: -1px; }
  .brand__sub { display: block; font-size: 26px; line-height: 1; margin-top: 20px; letter-spacing: 1px; }

  .trainer {
    position: absolute;
    left: 600px;
    top: 196px;
    width: 400px;
    text-align: center;
  }
  .trainer__name { font-size: 54px; font-weight: 400; line-height: 1.1; }
  .trainer__title { font-size: 28px; line-height: 1.15; margin-top: 4px; letter-spacing: 0.3px; }
  .trainer__cert { font-size: 23px; line-height: 1.35; }

  .contacts {
    position: absolute;
    left: 584px;
    top: 360px;
    list-style: none;
  }
  .contacts__item {
    display: flex;
    align-items: center;
    height: 52px;
    margin-bottom: 16px;
    font-size: 27px;
  }
  .contacts__icon { width: 52px; height: 52px; margin-right: 18px; flex-shrink: 0; }

  .back-art {
    position: absolute;
    left: 200px;
    top: 0;
    width: 420px;
    height: 587px;
    border-radius: 40% 60% 0 0;
    background: linear-gradient(180deg, rgba(255,255,255,0.35), rgba(238,109,146,0.12) 80%);
  }
  .back-leaf {
    position: absolute;
    left: 120px;
    top: 520px;
    width: 140px;
    height: 67px;
    border-radius: 50% 50% 0 0;
    background: radial-gradient(ellipse at center bottom, rgba(127,211,198,0.6), rgba(127,211,198,0) 70%);
  }

  .offer__headline {
    position: absolute;
    left: 0;
    top: 72px;
    width: 1021px;
    text-align: center;
    font-family: "Arimo", sans-serif;
    font-weight: 700;
    font-size: 38px;
    letter-spacing: -0.3px;
  }
  .offer__call {
    position: absolute;
    left: 0;
    top: 200px;
    width: 1021px;
    padding-left: 270px;
    text-align: center;
    font-family: "Arimo", sans-serif;
    font-size: 34px;
    line-height: 1.4;
  }
  .offer__call strong { font-weight: 700; }
  .offer__call--full { padding-left: 150px; }

  .services {
    position: absolute;
    left: 18px;
    top: 388px;
    list-style: none;
    font-family: "Arimo", sans-serif;
    font-size: 35px;
    line-height: 47.5px;
  }
  .services__item::before { content: "\2605"; font-size: 24px; margin-right: 12px; vertical-align: 3px; }
</style>
</head>
<body>
<main class="canvas">

  <section class="card card--front" aria-label="Front of business card">
    <svg class="backdrop" width="1021" height="585" viewBox="0 0 1021 585" aria-hidden="true">
      <path d="M470 0 H1021 V320 C930 300 860 250 800 190 C720 120 620 120 560 90 C510 60 480 30 470 0 Z" fill="var(--aqua)"/>
      <path d="M0 400 C60 390 120 430 170 480 C200 520 215 560 220 585 H0 Z" fill="var(--aqua)"/>
    </svg>
    <div class="figure-art" role="img" aria-label="Line illustration of a woman's profile with flowing hair"></div>
    <div class="leaf-art" role="img" aria-label="Small teal leaf sprig"></div>

    <div class="brand">
      <span class="brand__name">LumaStride</span>
      <span class="brand__sub">Studio</span>
    </div>

    <div class="trainer">
      <h1 class="trainer__name">Odette Calvo</h1>
      <p class="trainer__title">MASTER PERSONAL TRAINER</p>
      <p class="trainer__cert">Cert III &amp; Cert IV in Fitness</p>
      <p class="trainer__cert">Senior First Aid</p>
    </div>

    <ul class="contacts">
      <li class="contacts__item">
        <svg class="contacts__icon" viewBox="0 0 52 52" aria-hidden="true">
          <circle cx="26" cy="26" r="23" fill="none" stroke="var(--ink)" stroke-width="2.5"/>
          <path d="M19 14 l5 6 -3 3 c2 4 5 7 9 9 l3 -3 6 5 -3 4 c-9 0 -21 -12 -21 -21 z" fill="var(--ink)"/>
        </svg>
        <span>0493 507 618</span>
      </li>
      <li class="contacts__item">
        <svg class="contacts__icon" viewBox="0 0 52 52" aria-hidden="true">
          <circle cx="26" cy="26" r="23" fill="none" stroke="var(--ink)" stroke-width="2.5"/>
          <rect x="14" y="17" width="24" height="18" fill="none" stroke="var(--ink)" stroke-width="2.5"/>
          <path d="M14 17 L26 28 L38 17" fill="none" stroke="var(--ink)" stroke-width="2.5"/>
        </svg>
        <span>lumastride@quellmail.test</span>
      </li>
      <li class="contacts__item">
        <svg class="contacts__icon" viewBox="0 0 52 52" aria-hidden="true">
          <circle cx="26" cy="26" r="23" fill="none" stroke="var(--ink)" stroke-width="2.5"/>
        </svg>
        <span>LumaStride Studio</span>
      </li>
    </ul>
  </section>

  <section class="card card--back" aria-label="Back of business card">
    <div class="back-art" role="img" aria-label="Faint pink profile illustration"></div>
    <div class="back-leaf" role="img" aria-label="Small teal leaf sprig"></div>

    <h2 class="offer__headline">Need direction with your health &amp; fitness goals?</h2>
    <p class="offer__call">Call now for your <strong>free</strong></p>
    <p class="offer__call offer__call--full" style="top:248px;">1 on 1 Personal Training Session with full consultation</p>

    <ul class="services">
      <li class="services__item">Mobile Personal Training</li>
      <li class="services__item">Individual Sessions</li>
      <li class="services__item">Bootcamp</li>
      <li class="services__item">Weight-loss and Toning</li>
    </ul>
  </section>

</main>
</body>
</html>
```